Business Card, A4 Letter Head and DL Envelope for Vantrelle

We are looking for a design for our Business Card, A4 Letter Head and DL Envelope.

Vantrelle is a distributor of promotional products. We specialize in a range of branded promotional products, these include pens, polo shirts, key rings, drink bottles, uniforms and bags to name a few. We are experts in marketing and assist companies in choosing the right promotional product for their needs. We will predominately be an online business where customers visit our website and browse our range of promotional products and branding options.

Our colours are black, red, white and grey.

Files must be supplied in eps, pdf and ai format.

Please display the following information:
Corbin Hale
Account Manager
Suite xxx, 214 Dawlish Parade Melbourne, Victoria 3000
Phone +61 3 5550 1827
Mobile +61 455 501 936
sales@vantrelle.com.au
www.vantrelle.com.au

```html
<!DOCTYPE html>
<html lang="en">
<head>
<meta charset="utf-8">
<title>Vantrelle Business Card</title>
<link rel="stylesheet" href="https://fonts.googleapis.com/css2?family=Jost:wght@400;500;600&display=swap">
<style>
  :root {
    --backdrop: #000000;
    --card: #ffffff;
    --brand-red: #e8254a;
    --ink: #111111;
    --brand-grey: #5b5d61;
    --mark-grey: #b9bbbe;
  }
  * { margin: 0; padding: 0; box-sizing: border-box; }
  html, body {
    width: 1200px;
    height: 459px;
    overflow: hidden;
    background: var(--backdrop);
    font-family: "Jost", "Century Gothic", sans-serif;
  }
  .stage {
    position: relative;
    width: 1200px;
    height: 459px;
  }
  .card {
    position: absolute;
    top: 80px;
    width: 485px;
    height: 295px;
    background: var(--card);
  }
  .card--front { left: 98px; }
  .card--back { left: 616px; }

  .brand {
    position: absolute;
    left: 60px;
    top: 115px;
    display: flex;
    align-items: center;
    gap: 22px;
  }
  .brand__dot {
    width: 66px;
    height: 66px;
    border-radius: 50%;
    background: var(--mark-grey);
  }
  .brand__name {
    font-size: 40px;
    font-weight: 600;
    letter-spacing: 1px;
    color: var(--brand-grey);
    line-height: 1;
  }

  .contact {
    position: absolute;
    left: 38px;
    color: var(--ink);
    white-space: nowrap;
  }
  .contact__name {
    top: 40px;
    font-size: 19px;
    font-weight: 600;
    color: var(--brand-red);
  }
  .contact__role {
    top: 64px;
    font-size: 16px;
    font-weight: 400;
  }
  .contact__line {
    font-size: 14px;
    font-weight: 400;
  }
  .contact__phones { top: 148px; }
  .contact__address { top: 177px; }
  .contact__email { top: 205px; }
  .contact__web {
    top: 233px;
    font-weight: 600;
    color: var(--brand-red);
  }
  .label {
    font-weight: 500;
    color: var(--brand-red);
  }
  .divider { margin: 0 6px; }
</style>
</head>
<body>
<main class="stage">
  <section class="card card--front" aria-label="Business card front">
    <div class="brand">
      <span class="brand__dot"></span>
      <span class="brand__name">VANTRELLE</span>
    </div>
  </section>

  <section class="card card--back" aria-label="Business card back">
    <p class="contact contact__name">Corbin Hale</p>
    <p class="contact contact__role">Account Manager</p>
    <p class="contact contact__line contact__phones">
      <span class="label">Phone</span> +61 3 5550 1827<span class="divider">|</span><span class="label">Mobile</span> +61 455 501 936
    </p>
    <p class="contact contact__line contact__address">Suite xxx, 214 Dawlish Parade Melbourne, Victoria, 3000</p>
    <p class="contact contact__line contact__email">sales@vantrelle.com.au</p>
    <p class="contact contact__line contact__web">www.vantrelle.com.au</p>
  </section>
</main>
</body>
</html>
```